5'x15' banner for sustainable apartments

Meadow 457 is a sustainable community that focuses on well being of tenants and reduction of carbon footprint.
Need an eye catching banner to be displayed on the side of a building. Walls are gray (see pic), so it's a perfect canvass to splash some colors. Banner shall include the word "apartments" and represent sustainability (ie. sustainable apartments).
Please check website to see more about the community: www.meadow457.example
Dimensions are 5' W x 15' H.
Daily traffic is approx. 20k cars.

Target Market(s)

we target environmentally conscious tenants who want to live in a community of like-minded people. We have a community garden, and reuse "gray" water for irrigation. We've also implemented recycling programs.
We've also built a deck were we have yoga practices -free of charge- for our tenants and guests.

Industry/Entity Type

Community

Font styles to use
Other font styles liked:
• Leelawadee UI

Requirements
Must have
• Should be understood that these are apartments for rent.
• whatever imagery is to be used, should have a strong association with sustainability.
• If any text, use Leelawadee UI font.
Nice to have
• well being imagery / association
• The picture with the painted mural is not from the subject building, but liked the drawing, so could spark some idea.

```html
<!DOCTYPE html>
<html lang="en">
<head>
<meta charset="utf-8">
<title>Meadow 457 — Apartments Banner</title>
<link rel="stylesheet" href="https://fonts.googleapis.com/css2?family=Open+Sans:wght@400&display=swap">
<style>
  :root {
    --lime: #c8d22d;
    --lime-soft: #b9c63a;
    --leaf-deep: #3f6b2e;
    --leaf-mid: #6d9a3a;
    --bloom-pink: #d9478a;
    --bloom-orange: #e8602a;
    --white: #ffffff;
  }
  html, body {
    margin: 0;
    padding: 0;
    width: 1200px;
    height: 2258px;
    overflow: hidden;
    background: var(--lime);
  }
  .banner {
    position: relative;
    width: 1200px;
    height: 2258px;
    overflow: hidden;
    background: var(--lime);
    font-family: "Open Sans", "Segoe UI", sans-serif;
  }
  .flourish-backdrop,
  .nature-collage {
    position: absolute;
    top: 0;
    left: 0;
    width: 1200px;
    height: 2258px;
  }
  .vertical-text {
    position: absolute;
    margin: 0;
    white-space: nowrap;
    color: var(--white);
    font-weight: 400;
    line-height: 1;
    transform: rotate(90deg);
    transform-origin: top left;
  }
  .headline {
    left: 1152px;
    top: 58px;
    font-size: 330px;
    letter-spacing: -4px;
  }
  .tagline {
    left: 770px;
    top: 1105px;
    font-size: 106px;
    letter-spacing: -1px;
  }
</style>
</head>
<body>
<main class="banner">
  <svg class="flourish-backdrop" viewBox="0 0 1200 2258" role="img" aria-label="Faint swirling leaf flourish pattern in soft green across the background">
    <defs>
      <radialGradient id="flourishGlow" cx="50%" cy="50%" r="50%">
        <stop offset="0%" stop-color="#b9c63a" stop-opacity="0.55"/>
        <stop offset="100%" stop-color="#b9c63a" stop-opacity="0"/>
      </radialGradient>
    </defs>
    <ellipse cx="760" cy="1150" rx="520" ry="1100" fill="url(#flourishGlow)"/>
  </svg>

  <svg class="nature-collage" viewBox="0 0 1200 2258" role="img" aria-label="Collage of frangipani blossoms, lovebirds, a blackbird on a twig, agave, succulents and flowering cacti along the left edge">
    <defs>
      <linearGradient id="collageTone" x1="0" y1="0" x2="0" y2="1">
        <stop offset="0%" stop-color="#4c7a34"/>
        <stop offset="22%" stop-color="#6a9a3c"/>
        <stop offset="48%" stop-color="#557a4a"/>
        <stop offset="72%" stop-color="#6f9466"/>
        <stop offset="86%" stop-color="#c0568a"/>
        <stop offset="100%" stop-color="#6f8a4c"/>
      </linearGradient>
    </defs>
    <path d="M0 0 H620 C700 120 690 300 560 420 C520 560 540 760 470 980
             C560 1060 590 1200 520 1300 C420 1380 400 1460 410 1560
             C470 1620 500 1700 470 1820 C440 1920 330 1960 300 2060
             C300 2140 280 2210 260 2258 H0 Z" fill="url(#collageTone)"/>
  </svg>

  <h1 class="vertical-text headline">apartments</h1>
  <p class="vertical-text tagline">sustainable living</p>
</main>
</body>
</html>
```